Marlow Law Stationery - Letterhead, Envelopes, Business Cards

We need high quality business stationery for our Personal Injury Law Firm located in Houston, Texas. The design should include the logo, Marlow Law Group, PLLC, 713-555-4718, 2150 Fernbrook Avenue, Suite 310, Houston, Texas 77019 www.MarlowLaw.example. The colors are blue and white. The letterhead should also include the Attorneys - Tessa Quill, Mitchell R. Marlow and Derek Hale.

```html
<!DOCTYPE html>
<html lang="en">
<head>
<meta charset="utf-8">
<title>Marlow Law Letterhead</title>
<link href="https://fonts.googleapis.com/css2?family=Figtree:wght@400;500;600&family=League+Spartan:wght@700&display=swap" rel="stylesheet">
<style>
  :root {
    --backdrop: #e0e0e0;
    --paper: #ffffff;
    --navy: #1b2352;
    --band: #03143f;
    --rule-grey: #8a8a8a;
    --body-ink: #333333;
    --name-ink: #1b2a5c;
    --title-ink: #222222;
  }
  * { box-sizing: border-box; margin: 0; padding: 0; }
  html, body { width: 1200px; height: 1200px; overflow: hidden; }
  body { background: var(--backdrop); position: relative; font-family: "Figtree", sans-serif; }

  .letterhead {
    position: absolute; left: 216px; top: 76px; width: 768px; height: 1046px;
    background: var(--paper);
    box-shadow: 6px 8px 16px rgba(0,0,0,0.18);
  }

  .brand { position: absolute; left: 210px; top: 86px; display: flex; align-items: center; gap: 12px; }
  .brand-mark { width: 88px; height: 88px; border-radius: 50%; background: var(--navy); flex: none; }
  .brand-text { font-family: "League Spartan", sans-serif; font-weight: 700; color: var(--navy); text-align: center; line-height: 1; }
  .brand-firm { font-size: 16.5px; letter-spacing: 0.1px; }
  .brand-tagline { font-size: 37px; line-height: 32px; margin-top: 8px; letter-spacing: -0.3px; }
  .brand-tagline span { display: block; }

  .letter-body {
    position: absolute; left: 51px; top: 296px; width: 660px;
    font-size: 18.5px; line-height: 26px; color: var(--body-ink);
    text-align: justify; letter-spacing: -0.2px;
  }
  .letter-body p + p { margin-top: 26px; }
  .letter-body p:first-child { text-indent: 18px; }

  .attorneys { position: absolute; left: 119px; top: 897px; display: flex; align-items: center; }
  .attorney { padding: 0 19px; }
  .attorney:first-child { padding-left: 0; }
  .attorney + .attorney { border-left: 1.5px solid var(--title-ink); }
  .attorney-name { font-size: 20px; font-weight: 600; color: var(--name-ink); line-height: 21px; }
  .attorney-title { font-size: 14px; color: var(--title-ink); line-height: 16px; text-transform: uppercase; }

  .rule { position: absolute; left: 0; top: 952px; width: 100%; height: 6px; background: var(--rule-grey); }

  .contact-band {
    position: absolute; left: 0; top: 965px; width: 100%; height: 81px;
    background: var(--band); color: #fff; text-align: center;
    font-size: 19px; letter-spacing: 0.3px;
  }
  .contact-line { display: flex; justify-content: center; align-items: center; gap: 30px; margin-top: 14px; height: 24px; }
  .contact-item { display: flex; align-items: center; gap: 8px; }
  .contact-item svg { width: 20px; height: 20px; }
  .contact-address { margin-top: 3px; }
</style>
</head>
<body>
  <main class="letterhead">
    <header class="brand">
      <div class="brand-mark"></div>
      <div class="brand-text">
        <div class="brand-firm">MARLOW LAW GROUP, PLLC</div>
        <div class="brand-tagline"><span>INJURY</span><span>ATTORNEYS</span></div>
      </div>
    </header>

    <section class="letter-body">
      <p>Lorem ipsum dolor sit amet, consectetuer adipiscing elit, sed diam nonummy nibh euismod tincidunt ut laoreet dolore magna aliquam erat volutpat. Ut wisi enim ad minim veniam, quis nostrud exerci tation ullamcorper suscipit lobortis nisl ut aliquip ex ea commodo consequat. Duis autem vel eum iriure dolor in hendrerit in vulputate velit esse molestie consequat, vel illum dolore eu feugiat nulla facilisis at vero eros et accumsan et iusto odio dignissim qui blandit praesent luptatum zzril delenit augue duis dolore te feugait nulla facilisi.</p>
      <p>Lorem ipsum dolor sit amet, cons ectetuer adipiscing elit, sed diam nonummy nibh euismod tincidunt ut laoreet dolore magna aliquam erat volutpat. Ut wisi Lorem ipsum dolor sit amet, consectetuer adipiscing elit, sed diam nonummy nibh euismod tincidunt ut laoreet dolore magna aliquam erat volutpat. Ut wisi enim ad minim veniam, quis nostrud exerci tation ullamcorper suscipit lobortis nisl ut aliquip ex ea commodo consequat. Duis autem vel eum iriure dolor in hendrerit in vulputate velit esse molestie consequat,Lorem ipsum dolor sit amet, cons ectetuer adipiscing elit, sed diam nonummy nibh euismod tincidunt ut laoreet dolore magna aliquam erat volutpat.</p>
    </section>

    <section class="attorneys">
      <div class="attorney">
        <div class="attorney-name">Tessa Quill</div>
        <div class="attorney-title">Managing Partner</div>
      </div>
      <div class="attorney">
        <div class="attorney-name">Mitchell R. Marlow</div>
        <div class="attorney-title">Associate Attorney</div>
      </div>
      <div class="attorney">
        <div class="attorney-name">Derek Hale</div>
        <div class="attorney-title">Associate Attorney</div>
      </div>
    </section>

    <div class="rule"></div>

    <footer class="contact-band">
      <div class="contact-line">
        <span class="contact-item">
          <svg viewBox="0 0 24 24" aria-hidden="true"><path fill="#fff" d="M6.6 10.8a15.2 15.2 0 0 0 6.6 6.6l2.2-2.2a1 1 0 0 1 1-.25 11.4 11.4 0 0 0 3.6.57 1 1 0 0 1 1 1V20a1 1 0 0 1-1 1A17 17 0 0 1 3 4a1 1 0 0 1 1-1h3.5a1 1 0 0 1 1 1c0 1.25.2 2.45.57 3.57a1 1 0 0 1-.25 1z"/></svg>
          713-555-4718
        </span>
        <span class="contact-item">
          <svg viewBox="0 0 24 24" aria-hidden="true" fill="none" stroke="#fff" stroke-width="1.6"><circle cx="12" cy="12" r="9.5"/><ellipse cx="12" cy="12" rx="4.2" ry="9.5"/><path d="M2.5 12h19M4 7h16M4 17h16M12 2.5v19"/></svg>
          www.MarlowLaw.example
        </span>
      </div>
      <div class="contact-address">2150 Fernbrook Avenue, Suite 310, Houston, Texas 77019</div>
    </footer>
  </main>
</body>
</html>
```